Stationery Design Project

I am looking for stationary design for an automotive collision repair company. This needs to work with my business cards just designed here. I've attached. I need 8.5 x 11 stationary and corissponding envelopes. a post it note pad also. Our companies focus is very high end customer service driven . Our customer base is 35-65 middle to high income. Please include company name, logo, address, phone number, web address. The business card is two greys with green and white writing. I invision a light grey background with a darker grey band on it that contains the logo.

I justĀ 

Why is no one touching this project

Target Market(s)

60%. Women 40% men. Age 35-60

Industry/Entity Type

Automotive

Requirements
Must have
• Tie in with business cards. So it needs grey tones with green and white logo. Name, address, phone and web address. Must have 8.5 x 11 paper and envelopes.
Nice to have
• Post it notes

```html
<!DOCTYPE html>
<html lang="en">
<head>
<meta charset="utf-8">
<title>Panelcraft Stationery</title>
<link rel="stylesheet" href="https://fonts.googleapis.com/css2?family=Oswald:wght@600&family=Open+Sans:wght@400&display=swap">
<style>
  :root {
    --backdrop: #e6e6e4;
    --paper: #ffffff;
    --band-grey: #6d6e70;
    --band-dark: #3b3b3d;
    --brand-green: #8dc63f;
    --ink: #4a4a4c;
    --white: #ffffff;
  }
  * { margin: 0; padding: 0; box-sizing: border-box; }
  html, body { width: 1200px; height: 868px; overflow: hidden; }
  body {
    background: var(--backdrop);
    font-family: "Open Sans", Arial, sans-serif;
    position: relative;
  }
  .sheet {
    position: absolute;
    background: var(--paper);
    overflow: hidden;
    box-shadow: 0 2px 6px rgba(0,0,0,.18);
  }
  .sheet-header { position: absolute; left: 0; top: 0; width: 100%; display: block; }
  .brand-name {
    position: absolute;
    font-family: "Oswald", "Arial Narrow", sans-serif;
    font-weight: 600;
    color: var(--brand-green);
    line-height: 1;
    white-space: nowrap;
  }
  .contact-line {
    position: absolute;
    left: 0; right: 0;
    display: flex;
    justify-content: center;
    color: var(--ink);
    white-space: nowrap;
  }
  .contact-line span + span::before {
    content: "|";
    color: #b9b9b9;
    margin: 0 .6em;
  }

  /* Letterhead 8.5 x 11 */
  .letterhead { left: 65px; top: 105px; width: 505px; height: 652px; }
  .letterhead .sheet-header { height: 122px; }
  .letterhead .brand-name { left: 0; right: 0; top: 42px; text-align: center; font-size: 34px; padding-left: 120px; }
  .letterhead .contact-line { bottom: 14px; font-size: 6.3px; }

  /* Envelope */
  .envelope { left: 598px; top: 189px; width: 562px; height: 242px; }
  .envelope .sheet-header { height: 125px; }
  .envelope .brand-name { left: 42px; top: 34px; font-size: 30px; }
  .envelope .return-address {
    position: absolute; left: 42px; top: 73px;
    font-size: 7px; color: var(--white);
  }

  /* Note pad */
  .notepad { left: 598px; top: 470px; width: 237px; height: 305px; }
  .notepad .sheet-header { height: 56px; }
  .notepad .brand-name { left: 0; right: 0; top: 18px; text-align: center; font-size: 17px; padding-left: 50px; }
  .notepad .contact-line { bottom: 6px; font-size: 3px; }
</style>
</head>
<body>

<section class="sheet letterhead" aria-label="Letterhead">
  <svg class="sheet-header" viewBox="0 0 505 122" preserveAspectRatio="none" aria-hidden="true">
    <path d="M0 0H505V110C360 92 180 98 0 116Z" fill="var(--band-dark)"/>
    <path d="M0 0H505V98C360 84 180 92 0 102Z" fill="var(--band-grey)"/>
    <path d="M0 116C180 98 360 92 505 110" fill="none" stroke="var(--brand-green)" stroke-width="4"/>
  </svg>
  <div class="brand-name">Panelcraft</div>
  <p class="contact-line">
    <span>m. 0400 123 456</span><span>t. 03 5550 1200</span><span>f. 03 5550 1299</span><span>john@panelcraftauto.com</span><span>www.panelcraftauto.com</span><span>88 Mender Lane Fairhaven 2951</span>
  </p>
</section>

<section class="sheet envelope" aria-label="Envelope">
  <svg class="sheet-header" viewBox="0 0 562 125" preserveAspectRatio="none" aria-hidden="true">
    <path d="M0 0H562V94C400 86 200 96 0 114Z" fill="var(--band-dark)"/>
    <path d="M0 0H562V74C400 68 200 82 0 92Z" fill="var(--band-grey)"/>
    <path d="M0 114C200 96 400 86 562 94" fill="none" stroke="var(--brand-green)" stroke-width="4"/>
  </svg>
  <div class="brand-name">Panelcraft</div>
  <p class="return-address">88 Mender Lane Fairhaven 2951</p>
</section>

<section class="sheet notepad" aria-label="Note pad">
  <svg class="sheet-header" viewBox="0 0 237 56" preserveAspectRatio="none" aria-hidden="true">
    <path d="M0 0H237V47C170 40 90 44 0 52Z" fill="var(--band-dark)"/>
    <path d="M0 0H237V38C170 32 90 36 0 42Z" fill="var(--band-grey)"/>
    <path d="M0 52C90 44 170 40 237 47" fill="none" stroke="var(--brand-green)" stroke-width="2.5"/>
  </svg>
  <div class="brand-name">Panelcraft</div>
  <p class="contact-line">
    <span>m. 0400 123 456</span><span>t. 03 5550 1200</span><span>f. 03 5550 1299</span><span>john@panelcraftauto.com</span><span>panelcraftauto.com</span><span>88 Mender Lane Fairhaven 2951</span>
  </p>
</section>

</body>
</html>
```